lumenweave project business card, interior design and decoration firm

I'm a young woman and I've just created my interior design consulting firm. I'm very inspired by brasilian design, italian design, argentinian spirit, I like pure forms, chic colors (blue specially) and raw stuffs (wood, glass,
I work with wines properties, boats and yachts dealers, private people. Elegant but inspired
It's very important to dedicate one side to this card to the name Lumenweave. I would like my name on the other side (Claire-Anne Vobrel), my mail cavobrel@postvane.fr, my number + 33 6 91 35 20 86

Target Market(s)

middle and upper class, young people,

Contact Information for Business Card

Font styles to use
Sans Serif

Colors
0255a3
85abd2
000000
fdfdfd
86cfc6
fdf0f6
00a990
f04a50

Requirements
Must have
• The name Lumenweave, my name my number and mail one or two colors max, one logo if it's possible. AND uder The name Lumenweave "Cabinet de conseil en aménagement intérieur"

```html
<!DOCTYPE html>
<html lang="en">
<head>
<meta charset="utf-8">
<title>Lumenweave business card</title>
<link rel="stylesheet" href="https://fonts.googleapis.com/css2?family=Cinzel:wght@400;600&family=Open+Sans:ital,wght@1,400;1,700&display=swap">
<style>
  :root {
    --brand-blue: #1a4aa6;
    --accent-teal: #1a9aaa;
    --ink: #111111;
    --paper: #fdfdfd;
    --shade-grey: #d4d4da;
    --wood-dark: #3a2416;
    --wood-mid: #5a3a24;
    --title-light: #f3ead8;
    --page-bg: #e9e9ec;
  }
  html, body {
    margin: 0;
    width: 1200px;
    height: 1200px;
    overflow: hidden;
    background: var(--page-bg);
  }
  .sheet {
    position: relative;
    width: 1200px;
    height: 1200px;
  }
  .card {
    position: absolute;
    left: 150px;
    width: 900px;
    height: 515px;
    box-shadow: 0 12px 30px rgba(0,0,0,0.18);
  }
  .card--contact { top: 50px; }
  .card--brand { top: 630px; }
  .card svg { display: block; }
  .contact-name {
    font-family: "Cinzel", serif;
    font-weight: 600;
    font-size: 46px;
    fill: var(--brand-blue);
  }
  .contact-tagline, .brand-tagline {
    font-family: "Open Sans", sans-serif;
    font-style: italic;
    font-size: 26px;
  }
  .contact-tagline { fill: var(--accent-teal); }
  .contact-line {
    font-family: "Open Sans", sans-serif;
    font-style: italic;
    font-weight: 700;
    font-size: 24px;
    fill: var(--ink);
  }
  .contact-line--mail { font-weight: 400; font-size: 22px; }
  .contact-icon { fill: none; stroke: var(--accent-teal); stroke-width: 2.6; stroke-linecap: round; }
  .brand-name {
    font-family: "Cinzel", serif;
    font-weight: 400;
    font-size: 74px;
    letter-spacing: 2px;
    fill: var(--title-light);
  }
  .brand-tagline { fill: var(--paper); font-size: 24px; }
</style>
</head>
<body>
<main class="sheet">

  <!-- Contact side -->
  <section class="card card--contact" aria-label="Card back with contact details">
    <svg width="900" height="515" viewBox="0 0 900 515">
      <defs>
        <linearGradient id="g-interior" x1="0" y1="0" x2="1" y2="1">
          <stop offset="0" stop-color="#d9c6ad"/><stop offset="0.5" stop-color="#a57a55"/><stop offset="1" stop-color="#6b4a34"/>
        </linearGradient>
        <linearGradient id="g-bouquet" x1="0" y1="0" x2="1" y2="1">
          <stop offset="0" stop-color="#6f8b4e"/><stop offset="0.5" stop-color="#e05a8f"/><stop offset="1" stop-color="#8a6a4e"/>
        </linearGradient>
        <linearGradient id="g-roses" x1="0" y1="0" x2="1" y2="1">
          <stop offset="0" stop-color="#eef0ee"/><stop offset="0.5" stop-color="#eeaab8"/><stop offset="1" stop-color="#4f7a3c"/>
        </linearGradient>
        <linearGradient id="g-shelf" x1="0" y1="0" x2="1" y2="1">
          <stop offset="0" stop-color="#2a2a30"/><stop offset="0.6" stop-color="#3a3028"/><stop offset="1" stop-color="#b8893e"/>
        </linearGradient>
      </defs>
      <rect width="900" height="515" fill="url(#g-interior)" role="img" aria-label="Photo of a dining table with glassware and dried flowers"/>
      <polygon points="330,320 760,330 720,515 330,515" fill="url(#g-roses)" role="img" aria-label="Photo of pink camellias in a vase"/>
      <polygon points="720,330 900,300 900,515 720,515" fill="url(#g-shelf)" role="img" aria-label="Photo of a dark shelf with a gilded mirror"/>
      <polygon points="660,110 900,160 900,300 700,330" fill="url(#g-bouquet)" role="img" aria-label="Photo of a bouquet of orchids and gerberas"/>
      <polygon points="90,0 560,0 700,110 700,330 250,310 30,150" fill="var(--paper)"/>
      <polygon points="560,0 700,110 700,330 600,200" fill="var(--shade-grey)" opacity="0.8"/>
      <polygon points="0,0 90,0 30,150 250,310 0,200" fill="var(--brand-blue)"/>
      <polygon points="760,40 900,0 900,160 820,150" fill="var(--brand-blue)"/>
      <text class="contact-name" x="110" y="110">Claire-Anne Vobrel</text>
      <text class="contact-tagline" x="210" y="152">interior design consulting firm</text>
      <path class="contact-icon" d="M352 190 q-8 10 0 22 q4 4 8 2"/>
      <text class="contact-line" x="372" y="212">+33 6 91 35 20 86</text>
      <circle class="contact-icon" cx="356" cy="250" r="7"/>
      <text class="contact-line contact-line--mail" x="380" y="258">cavobrel@postvane.fr</text>
    </svg>
  </section>

  <!-- Brand side -->
  <section class="card card--brand" aria-label="Card front with the firm name">
    <svg width="900" height="515" viewBox="0 0 900 515">
      <defs>
        <linearGradient id="g-wood" x1="0" y1="0" x2="1" y2="1">
          <stop offset="0" stop-color="var(--wood-dark)"/><stop offset="0.5" stop-color="var(--wood-mid)"/><stop offset="1" stop-color="var(--wood-dark)"/>
        </linearGradient>
        <linearGradient id="g-interior2" x1="0" y1="0" x2="1" y2="1">
          <stop offset="0" stop-color="#e2d2bc"/><stop offset="0.5" stop-color="#b0825a"/><stop offset="1" stop-color="#6b4a34"/>
        </linearGradient>
        <linearGradient id="g-bouquet2" x1="0" y1="0" x2="1" y2="1">
          <stop offset="0" stop-color="#7a6a54"/><stop offset="0.5" stop-color="#e05a8f"/><stop offset="1" stop-color="#6f8b4e"/>
        </linearGradient>
        <linearGradient id="g-roses2" x1="0" y1="0" x2="1" y2="1">
          <stop offset="0" stop-color="#e6e8e6"/><stop offset="0.5" stop-color="#eeaab8"/><stop offset="1" stop-color="#4f7a3c"/>
        </linearGradient>
      </defs>
      <rect width="900" height="515" fill="#2a2a34" role="img" aria-label="Photo of a dark shelf with a gilded mirror"/>
      <polygon points="0,140 150,90 280,515 0,515" fill="url(#g-interior2)" role="img" aria-label="Photo of a dining table with glassware and dried flowers"/>
      <polygon points="230,380 600,300 640,420 300,470" fill="url(#g-roses2)" role="img" aria-label="Photo of pink camellias in a vase"/>
      <polygon points="600,260 900,200 900,450 640,420" fill="url(#g-bouquet2)" role="img" aria-label="Photo of a bouquet of orchids and gerberas"/>
      <polygon points="470,0 560,0 900,170 900,200" fill="var(--paper)"/>
      <polygon points="0,0 200,0 0,120" fill="var(--brand-blue)"/>
      <polygon points="560,0 900,0 900,170" fill="var(--brand-blue)"/>
      <polygon points="150,40 480,0 640,300 230,400" fill="url(#g-wood)" role="img" aria-label="Photo of dark walnut wood grain"/>
      <text class="brand-name" x="190" y="200">Lumenweave</text>
      <text class="brand-tagline" x="250" y="245">interior design consulting firm</text>
    </svg>
  </section>

</main>
</body>
</html>
```